Stationery Design Project

We are looking for a full revision of our existing stationary to include within this project:

- Letterhead
- Business card
- Compliment slip

The items should be a reflection of our new website which can be found at http://www.larkfieldchecks.co.uk/

Our logo files are included within the file brief

There are some further projects which we may approach the winning designer for as we need a revision to the front cover of our reports, a new price list and two brochures for specific target markets.

Industry/Entity Type

Business

```html
<!DOCTYPE html>
<html lang="en">
<head>
<meta charset="utf-8">
<title>Larkfield Checks – Business Card</title>
<link rel="stylesheet" href="https://fonts.googleapis.com/css2?family=Lato:wght@400;700&display=swap">
<style>
  :root {
    --page-bg: #e9edf1;
    --card-white: #ffffff;
    --band-blue: #1d5fc8;
    --band-navy: #0c1a78;
    --text-dark: #2b2b2b;
    --brand-navy: #14237f;
    --icon-blue: #1c4fb0;
  }
  * { box-sizing: border-box; margin: 0; padding: 0; }
  html, body {
    width: 1200px; height: 960px; overflow: hidden;
    background: var(--page-bg);
    font-family: "Lato", Arial, sans-serif;
  }
  .sheet {
    width: 1200px; height: 960px;
    display: flex; flex-direction: column; align-items: center; justify-content: center;
    gap: 34px;
  }
  .card {
    position: relative;
    width: 760px; height: 434px;
    background: var(--card-white);
    box-shadow: 0 6px 20px rgba(20, 30, 60, 0.18);
    overflow: hidden;
  }
  .band-top { position: absolute; left: 0; right: 0; top: 0; height: 24px; background: var(--band-blue); }
  .band-bottom { position: absolute; left: 0; right: 0; bottom: 0; height: 40px; background: var(--band-navy); }
  .card-back .band-top { height: 30px; }
  .card-back .band-bottom { height: 72px; }

  .holder { position: absolute; left: 44px; top: 104px; color: var(--text-dark); }
  .holder-name { font-size: 40px; font-weight: 400; letter-spacing: 0.2px; }
  .holder-role { font-size: 24px; margin-top: 6px; }

  .contact-list { position: absolute; left: 44px; top: 222px; list-style: none; color: var(--text-dark); }
  .contact-list li { display: flex; align-items: center; gap: 14px; font-size: 21px; height: 32px; }
  .contact-list svg { width: 22px; height: 22px; flex: none; }
  .contact-web { font-weight: 700; }

  .address { position: absolute; left: 44px; top: 316px; font-size: 22px; line-height: 1.3; color: var(--text-dark); }

  .brand-name {
    font-family: "Lato", Arial, sans-serif;
    font-weight: 700;
    color: var(--brand-navy);
    text-transform: uppercase;
    letter-spacing: 1px;
  }
  .card-front .brand-name { position: absolute; right: 36px; bottom: 74px; font-size: 30px; }
  .card-back .brand-name {
    position: absolute; left: 0; right: 0; top: 150px;
    text-align: center; font-size: 56px;
  }
</style>
</head>
<body>
<main class="sheet">
  <section class="card card-front" aria-label="Business card front">
    <div class="band-top"></div>
    <div class="holder">
      <p class="holder-name">Maren Holloway</p>
      <p class="holder-role">Chief Innovator</p>
    </div>
    <ul class="contact-list">
      <li>
        <svg viewBox="0 0 24 24" aria-hidden="true"><rect x="3" y="2" width="18" height="20" rx="2" fill="none" stroke="var(--icon-blue)" stroke-width="2"/><rect x="6" y="5" width="12" height="5" fill="var(--icon-blue)"/><circle cx="8" cy="14" r="1.3" fill="var(--icon-blue)"/><circle cx="12" cy="14" r="1.3" fill="var(--icon-blue)"/><circle cx="16" cy="14" r="1.3" fill="var(--icon-blue)"/><circle cx="8" cy="18" r="1.3" fill="var(--icon-blue)"/><circle cx="12" cy="18" r="1.3" fill="var(--icon-blue)"/><circle cx="16" cy="18" r="1.3" fill="var(--icon-blue)"/></svg>
        <span>08450 772 418</span>
      </li>
      <li>
        <svg viewBox="0 0 24 24" aria-hidden="true"><rect x="2" y="5" width="20" height="14" fill="none" stroke="var(--icon-blue)" stroke-width="2"/><path d="M2 5l10 8 10-8M2 19l7-7M22 19l-7-7" fill="none" stroke="var(--icon-blue)" stroke-width="2"/></svg>
        <span>mail@larkfieldchecks.co.uk</span>
      </li>
      <li>
        <svg viewBox="0 0 24 24" aria-hidden="true"><path d="M12 3L2 12h3v9h5v-6h4v6h5v-9h3z" fill="var(--icon-blue)"/></svg>
        <span class="contact-web">www.larkfieldchecks.co.uk</span>
      </li>
    </ul>
    <p class="address">24 Meadow Lane<br>Brookfield, SC 29612</p>
    <p class="brand-name">Larkfield Checks</p>
    <div class="band-bottom"></div>
  </section>

  <section class="card card-back" aria-label="Business card back">
    <div class="band-top"></div>
    <p class="brand-name">Larkfield Checks</p>
    <div class="band-bottom"></div>
  </section>
</main>
</body>
</html>
```